Bref créative
bussines card and stationary
paper letterhead
Bright & Fun-filled
tavirel cusan
managing partner
14 lunca verde street, sector 3 Bucharest Romania
tavirel@plumvox.com
www.plumvox.com
The card will be printed on the very best paper there is.will use 500g paper to be thick and heavy.
I want when someone recieves the card to feel like - waaaaawww this is top quality business card - the printing,the paper, the attention to details - everyting is just perfect.
The company develiopes software for mobile phones, various applications dedicated to sport industry.The most important one "plumvox" will be rewinding recorded videos from various sports. In all the products launched by this company a LOT of attentions is offered to all the details - so that the final product is extremelly well designed, top quality and extremely reliable.
this is what the card needs to suggest as well - attention to details, professionalism and top quality.
Use the back for adquate graphics, drawings etc .Be creative.Impress!
logo
logo ai

```html
<!DOCTYPE html>
<html lang="en">
<head>
<meta charset="utf-8">
<title>plumvox stationery</title>
<link rel="stylesheet" href="https://fonts.googleapis.com/css2?family=Montserrat:wght@600;700&family=Open+Sans:wght@400;600&display=swap">
<style>
  :root {
    --brand-red: #e31e26;
    --paper: #ffffff;
    --ink: #3a3a3a;
    --ink-soft: #7a7a7a;
    --ghost: #ececec;
    --stage: #e6e6e6;
  }
  * { box-sizing: border-box; margin: 0; padding: 0; }
  html, body { width: 1200px; height: 850px; overflow: hidden; }
  body { background: var(--stage); font-family: "Open Sans", sans-serif; color: var(--ink); position: relative; }

  .card, .letterhead { position: absolute; background: var(--paper); box-shadow: 0 2px 8px rgba(0,0,0,.18); overflow: hidden; }

  .card { width: 340px; height: 195px; left: 175px; border-radius: 10px; }
  .card--front { top: 225px; }
  .card--back { top: 440px; background: var(--brand-red); }

  .brand { display: flex; flex-direction: column; align-items: center; position: absolute; }
  .brand__mark { border-radius: 50%; background: var(--brand-red); }
  .brand__name { font-family: "Montserrat", sans-serif; font-weight: 700; color: var(--brand-red); letter-spacing: .5px; line-height: 1; }

  .card--front .brand { left: 22px; top: 24px; }
  .card--front .brand__mark { width: 46px; height: 46px; }
  .card--front .brand__name { font-size: 20px; margin-top: 8px; }

  .ghost-circle { position: absolute; border-radius: 50%; background: var(--ghost); }
  .card--front .ghost-circle { width: 120px; height: 120px; right: 18px; top: 16px; }

  .holder { position: absolute; left: 150px; top: 100px; }
  .holder__name { font-family: "Montserrat", sans-serif; font-weight: 700; font-size: 12px; color: var(--brand-red); text-transform: capitalize; }
  .holder__role { font-size: 8px; color: var(--ink-soft); text-transform: capitalize; }

  .card-address { position: absolute; left: 22px; top: 150px; font-size: 7px; line-height: 1.4; color: var(--ink-soft); }
  .card-contact { position: absolute; left: 150px; top: 150px; font-size: 7px; line-height: 1.4; color: var(--ink-soft); }

  .card--back .brand { left: 50%; top: 38px; transform: translateX(-50%); }
  .card--back .brand__mark { width: 68px; height: 68px; background: var(--paper); }
  .card--back .brand__name { display: none; }
  .card--back .web { position: absolute; left: 0; right: 0; top: 145px; text-align: center; font-family: "Montserrat", sans-serif; font-weight: 600; font-size: 11px; color: var(--paper); letter-spacing: .6px; }

  .letterhead { width: 420px; height: 594px; left: 585px; top: 128px; }
  .letterhead .brand { left: 28px; top: 30px; }
  .letterhead .brand__mark { width: 38px; height: 38px; }
  .letterhead .brand__name { font-size: 16px; margin-top: 6px; }
  .letterhead__address { position: absolute; left: 28px; top: 108px; font-size: 7px; line-height: 1.4; color: var(--ink-soft); }
  .letterhead .ghost-circle { width: 250px; height: 250px; left: 85px; top: 235px; background: #f2f2f2; }
  .letterhead__footer { position: absolute; left: 28px; bottom: 28px; padding-left: 8px; border-left: 2px solid var(--brand-red); font-size: 6.5px; line-height: 1.5; color: var(--ink-soft); }
  .letterhead__web { position: absolute; left: 28px; bottom: 14px; font-size: 6.5px; color: var(--ink-soft); }
</style>
</head>
<body>

  <section class="card card--front">
    <div class="ghost-circle" aria-hidden="true"></div>
    <div class="brand">
      <span class="brand__mark" aria-hidden="true"></span>
      <span class="brand__name">plumvox</span>
    </div>
    <div class="holder">
      <p class="holder__name">tavirel cusan</p>
      <p class="holder__role">managing partner</p>
    </div>
    <p class="card-address">14 lunca verde street,<br>sector 3 Bucharest Romania</p>
    <p class="card-contact">T: +40 721 555 018<br>E: tavirel@plumvox.com</p>
  </section>

  <section class="card card--back">
    <div class="brand">
      <span class="brand__mark" aria-hidden="true"></span>
      <span class="brand__name">plumvox</span>
    </div>
    <p class="web">www.plumvox.com</p>
  </section>

  <section class="letterhead">
    <div class="brand">
      <span class="brand__mark" aria-hidden="true"></span>
      <span class="brand__name">plumvox</span>
    </div>
    <p class="letterhead__address">14 lunca verde street,<br>sector 3 Bucharest Romania</p>
    <div class="ghost-circle" aria-hidden="true"></div>
    <p class="letterhead__footer">T: +40 721 555 018<br>E: tavirel@plumvox.com</p>
    <p class="letterhead__web">www.plumvox.com</p>
  </section>

</body>
</html>
```